Flyer-Design für Hilfe zur Digitalisierung von Unternehmen
Vielen Dank für den schnellen Entwurf & die kurzfristigen Änderungen! Top!
Zielgruppe
Marketing
Schwerpunkte: Websites, Webshops, Travik Ads, Social Ads
Zielgruppe: kleine & mittelständische Unternehmen
Aufgabenstellung
Text bitte nur Inhaltlich übernehmen, bin nicht der große Poet! ;-)
Digitalisierung des Unternehmens / Im Zuge der aktuellen Lage # Corona , ist die Digitalisierung wieder ein Stück weiter ins Zentrum unseres Leben gerückt / Wir wollen Ihnen helfen auch Ihr Geschäft zu Digitalisieren, / In diesem Zuge haben wir ein einmaliges Angebot für Sie gestrickt. Ein voll funktionsfähigen Online Shop inkl. der ersten 5 Artikel ab 1999,00 €
weitere Angebote:
Webshops inkl. 5 Artikeln 1999,00
Website 5 Seiten 799,00
Travik Ads ab 60,00 mtl. keine Setup Gebühr
Social Ads ab 60,00 mtl. keine Setup Gebühr
für mehr Information können Sie uns gerne Kontaktieren / bzw ein persönlichen Termin vor Ort vereinbaren

```html
<!DOCTYPE html>
<html lang="de">
<head>
<meta charset="utf-8">
<title>Norvel Marketing GmbH – Flyer Digitalisierung</title>
<link rel="stylesheet" href="https://fonts.googleapis.com/css2?family=Open+Sans:wght@400;600;700&family=Source+Sans+3:wght@400;600;700&display=swap">
<style>
  :root {
    --night-blue: #0b1a4a;
    --deep-blue: #1636a8;
    --band-teal: rgba(90, 170, 190, 0.55);
    --sky-light: #acd9e6;
    --petrol: #1a566e;
    --text-grey: #4a4a4a;
    --accent-text: #1d5a72;
    --white: #ffffff;
    --logo-blue: #2aa6dc;
  }
  * { margin: 0; padding: 0; box-sizing: border-box; }
  html, body { width: 851px; height: 1200px; overflow: hidden; background: var(--white); }
  .flyer {
    position: relative;
    width: 851px;
    height: 1200px;
    overflow: hidden;
    background: var(--white);
    font-family: "Source Sans 3", "Open Sans", sans-serif;
  }
  .flyer__shapes { position: absolute; inset: 0; }
  .headline {
    position: absolute;
    left: 38px;
    top: 28px;
    color: var(--white);
    font-family: "Open Sans", sans-serif;
    font-weight: 400;
    font-size: 75px;
    line-height: 97px;
    letter-spacing: 0.3px;
  }
  .slogan {
    position: absolute;
    left: 38px;
    top: 526px;
    color: var(--white);
    font-family: "Open Sans", sans-serif;
    font-weight: 600;
    font-size: 43px;
    white-space: nowrap;
    transform-origin: left bottom;
    transform: rotate(-21.3deg);
  }
  .brand {
    position: absolute;
    left: 418px;
    top: 528px;
    display: flex;
    align-items: flex-start;
    gap: 16px;
  }
  .brand__square {
    flex: none;
    width: 38px;
    height: 38px;
    margin-top: 14px;
    background: var(--logo-blue);
  }
  .brand__name {
    color: var(--text-grey);
    font-family: "Source Sans 3", sans-serif;
    font-weight: 600;
    font-size: 46px;
    line-height: 60px;
    letter-spacing: 0.5px;
    text-transform: uppercase;
    white-space: nowrap;
  }
  .intro {
    position: absolute;
    left: 34px;
    top: 670px;
    width: 780px;
    color: var(--text-grey);
    font-size: 32.5px;
    line-height: 41.2px;
    letter-spacing: -0.4px;
  }
  .intro strong { color: var(--accent-text); font-weight: 600; }
  .offer {
    position: absolute;
    color: var(--white);
    font-family: "Open Sans", sans-serif;
    font-weight: 400;
    font-size: 43px;
    white-space: nowrap;
    transform-origin: left bottom;
    transform: rotate(-9.5deg);
  }
  .offer--line1 { left: 64px; top: 1044px; }
  .offer--line2 { left: 76px; top: 1100px; }
  .price {
    position: absolute;
    left: 558px;
    top: 1090px;
    color: var(--white);
    font-family: "Open Sans", sans-serif;
    font-size: 56px;
    white-space: nowrap;
  }
</style>
</head>
<body>
<main class="flyer">
  <svg class="flyer__shapes" width="851" height="1200" viewBox="0 0 851 1200">
    <defs>
      <linearGradient id="cityGlow" x1="0" y1="0" x2="1" y2="1">
        <stop offset="0" stop-color="#0a1745"/>
        <stop offset="0.45" stop-color="#1a3cb4"/>
        <stop offset="1" stop-color="#0c2a5e"/>
      </linearGradient>
    </defs>
    <polygon role="img" aria-label="Nächtliche Stadtsilhouette mit leuchtendem Binärcode-Globus" points="0,0 851,0 851,329 0,649" fill="url(#cityGlow)"/>
    <polygon class="slogan-band" points="0,494 851,182 851,329 0,649" fill="var(--band-teal)"/>
    <polygon class="light-wedge" points="158,594 851,329 851,852" fill="var(--sky-light)"/>
    <polygon class="offer-band" points="0,1050 851,923 851,1200 0,1200" fill="var(--petrol)"/>
  </svg>

  <h1 class="headline">Verkaufen Sie<br>online . . .</h1>

  <p class="slogan">Digitalisieren Sie Ihr Unternehmen jetzt!</p>

  <div class="brand">
    <span class="brand__square"></span>
    <span class="brand__name">Norvel<br>Marketing GmbH</span>
  </div>

  <p class="intro">
    Gerade jetzt in dieser<br>
    schwierigen Zeit ist es <strong>wichtig<br>ihr Unternehmen zu digitalisieren,</strong><br>
    denn Ihre Kunden sind auf Ihren <strong>Online-Service</strong><br>
    angewiesen.<br>
    Wir unterstützen Sie dabei und haben extra für diese<br>
    Zeit ein besonmdere Angebote<br>
    für Sie
  </p>

  <p class="offer offer--line1">Ein voll funktionsfähigen Online Shop</p>
  <p class="offer offer--line2">inkl. der ersten 5 Artikel ab</p>
  <p class="price">1999,00 €</p>
</main>
</body>
</html>
```